Real Estate Listing Landing Page

I am looking for a landing page for my Flat Fee MLS Listing website... The name of my website is "Brightkey Home Sales".

I am a big fan of this landing page setup and would like something similar.
https://quaylinehomes.com/

I am a fan of the design style on https://quaylinehomes.com/ and also this design style as well... https://2817.velmontedge.com/

Use your creativity and incorporate your own twists that you would feel lift up this landing pages' appeal. I'd love some red color incorporated within the design.

Target Market(s)

Real Estate Home Sellers

Industry/Entity Type

Real Estate

Coding

Coded - Design and coding required

Font styles to use
Sans Serif

Colors
0054AA
0677BA
7BADD7
CADEEF
E8F1F8
0094D4
00A9DD
6FCCEA
C7EBF8
E9F6FB
EB3D1F
EC4F4E
F09395
F8D3D4
FCEDEE

```html
<!DOCTYPE html>
<html lang="en">
<head>
<meta charset="utf-8">
<title>Brightkey Home Sales – Flat Fee MLS Listing</title>
<link href="https://fonts.googleapis.com/css2?family=Poppins:wght@400;500;600;700;800&family=Montserrat:wght@400;500;600&display=swap" rel="stylesheet">
<style>
:root{
  --navy:#0c3f9a;
  --blue:#0054AA;
  --blue-mid:#0677BA;
  --blue-soft:#7BADD7;
  --blue-pale:#CADEEF;
  --blue-wash:#E8F1F8;
  --red:#EB3D1F;
  --red-soft:#EC4F4E;
  --red-light:#F09395;
  --ink:#1d2a44;
  --grey:#6b7280;
  --white:#fff;
}
*{box-sizing:border-box;margin:0;padding:0}
html,body{width:1200px;height:4922px;overflow:hidden}
body{font-family:"Montserrat",sans-serif;color:var(--ink);background:var(--white);position:relative}
.abs{position:absolute}
h1,h2,h3,h4,.btn,.brand{font-family:"Poppins",sans-serif}
.accent{color:var(--red)}
.btn{position:absolute;display:flex;align-items:center;justify-content:center;color:#fff;font-weight:600;font-size:15px;letter-spacing:.3px;text-decoration:none}
.btn-red{background:var(--red-soft)}
.btn-blue{background:var(--blue)}
.section-title{font-size:34px;font-weight:700;color:var(--blue);letter-spacing:-.3px;text-align:center;line-height:1.3}
.lorem{font-size:15.5px;line-height:21.5px;color:var(--grey)}

/* header */
.topline{top:0;left:0;width:1200px;height:5px;background:var(--red)}
.brand{font-weight:700;color:var(--blue);font-size:28px;line-height:32px;display:flex;align-items:center;gap:10px}
.brand .dot{width:16px;height:16px;background:var(--red);flex:none}
.header .brand{left:127px;top:30px;width:200px}
.utility{top:28px;right:135px;display:flex;gap:40px;font-size:14px;color:var(--grey);align-items:center}
.mainnav{top:78px;left:340px;display:flex;gap:32px;font-family:"Poppins",sans-serif;font-weight:600;font-size:14.5px;color:var(--ink)}

/* hero */
.hero{top:118px;left:0;width:1200px;height:599px;background:linear-gradient(180deg,#3f71c1 0%,#6b99d6 45%,#9cb8d9 62%,#5a5d5e 100%)}
.hero h1{left:127px;top:95px;font-size:40px;line-height:44px;color:#fff;font-weight:700}
.hero p{left:127px;top:195px;font-size:17px;line-height:21px;color:#fff;font-family:"Poppins",sans-serif;font-weight:500}
.hero .b1{left:127px;top:262px;width:147px;height:48px}
.hero .b2{left:284px;top:262px;width:176px;height:48px}

/* about */
.ring{border-radius:50%;border:2px solid var(--red-soft)}
.photo{border-radius:50%;overflow:hidden}
.about-title{left:577px;top:826px;font-size:35px;font-weight:700;color:var(--blue)}
.about-text{left:579px;top:886px;width:475px}

/* packages */
.packages{top:1318px;left:0;width:1200px;height:732px;background:linear-gradient(135deg,#0a5fc0 0%,#0c3f9a 60%,#1b2f86 100%)}
.packages h2{top:60px;left:0;width:1200px;color:#fff;font-size:34px}
.card{top:205px;width:297px;height:440px;background:#fff;border-radius:22px;text-align:center}
.price{left:90px;top:-60px;width:118px;height:118px;border-radius:50%;background:rgba(236,79,78,.3);display:flex;align-items:center;justify-content:center}
.price span{width:98px;height:98px;border-radius:50%;background:var(--red-soft);color:#fff;font-family:"Poppins",sans-serif;font-weight:700;font-size:28px;display:flex;align-items:center;justify-content:center}
.price sup{font-size:13px;margin-right:4px}
.card h3{margin-top:78px;font-size:26px;font-weight:700;color:var(--ink)}
.card p{margin-top:16px;font-size:15.5px;line-height:26.5px;color:var(--grey)}
.card .btn{left:82px;top:345px;width:134px;height:42px;font-size:14.5px}
.card a.more{position:absolute;left:0;width:100%;top:397px;font-size:16px;color:var(--blue);text-decoration:underline}

/* steps */
.step h4{font-size:19.5px;line-height:20px;color:var(--blue);font-weight:700}
.step p{font-size:14px;line-height:19px;color:var(--grey);margin-top:8px}
.step.left{text-align:right}
.icon{width:96px;height:96px;border-radius:50%;background:var(--red-soft);box-shadow:0 0 0 8px rgba(236,79,78,.18);display:flex;align-items:center;justify-content:center}

/* sold */
.sold{top:2729px;left:0;width:1200px;height:628px;background:var(--blue-wash)}
.sold h2{top:85px;width:1200px}
.tag{background:var(--red-soft);color:#fff;padding:0 6px}
.prop-img{top:170px;width:298px;height:198px}
.prop-box{top:368px;width:270px;height:160px;background:#fff;text-align:center;padding-top:18px}
.prop-box .val{font-family:"Poppins",sans-serif;font-size:27px;font-weight:700;color:var(--blue);line-height:28px}
.prop-box .cap{font-size:11.5px;color:var(--grey)}
.prop-box .desc{font-size:14.5px;line-height:19px;color:var(--grey);margin-top:12px}
.prop-box .rate{font-size:13px;font-weight:600;color:var(--red);margin-top:10px}

/* service */
.service-title{left:127px;top:3500px;font-size:35px;font-weight:700;color:var(--red-soft)}
.service-text{left:127px;top:3565px;width:330px}
.loc-card{left:492px;top:3565px;width:160px;height:78px;background:#fff;box-shadow:0 4px 16px rgba(0,40,100,.14);border-radius:6px;padding:12px 14px}
.loc-card b{font-family:"Poppins",sans-serif;font-size:14px;color:var(--blue)}
.loc-card p{font-size:10.5px;line-height:13px;color:var(--grey);margin-top:3px}

/* contact */
.contact{top:3927px;left:0;width:1200px;height:554px;background:linear-gradient(180deg,#e44c45 0%,#d83a36 100%)}
.contact h2{left:616px;top:82px;font-size:35px;color:#fff;font-weight:700}
.contact .intro{left:617px;top:132px;width:400px;font-size:13.5px;line-height:18px;color:#fff}
.field{position:absolute;background:#fff;border:1px solid #e0e0e0;font-size:13.5px;color:#444;padding:13px 12px}
.contact .submit{left:617px;top:4377px;width:116px;height:46px;background:var(--navy)}

/* footer */
.footer .brand{left:127px;top:4623px;width:200px}
.fcol h4{font-size:19px;font-weight:600;letter-spacing:1px;color:var(--ink)}
.fcol ul{list-style:none;margin-top:14px;font-size:14.5px;line-height:25.5px;color:#444}
.cinfo{display:flex;gap:12px;margin-top:12px;font-size:14px;line-height:17px;color:#444}
.cinfo .ci{width:30px;height:30px;border-radius:50%;background:var(--blue);flex:none;display:flex;align-items:center;justify-content:center}
.divider{left:127px;top:4797px;width:946px;height:1px;background:#dde3ea}
.social{left:127px;top:4842px;display:flex;gap:22px}
.social span{width:22px;height:22px;border-radius:50%;background:var(--ink)}
.copy{right:127px;top:4847px;font-size:13.5px;color:#444}
</style>
</head>
<body>

<div class="abs topline"></div>
<header class="header">
  <div class="abs brand"><span class="dot"></span>Brightkey Home Sales</div>
  <div class="abs utility"><span>Help Center</span><span>Listing Dashboard</span>
    <span style="color:var(--ink)"><svg width="13" height="13" viewBox="0 0 13 13"><circle cx="6.5" cy="4" r="3" fill="#EB3D1F"/><path d="M1 13c0-3.5 2.5-5 5.5-5s5.5 1.5 5.5 5z" fill="#EB3D1F"/></svg> Login</span>
    <svg width="16" height="16" viewBox="0 0 16 16"><circle cx="6.5" cy="6.5" r="4.5" fill="none" stroke="#EB3D1F" stroke-width="2.2"/><path d="M10 10l4 4" stroke="#EB3D1F" stroke-width="2.4"/></svg>
  </div>
  <nav class="abs mainnav"><span>HOW IT WORKS</span><span>PRICING</span><span>WHY WE'RE BETTER</span><span>LIST YOUR HOME</span><span>CONTACT US</span></nav>
</header>

<section class="abs hero" role="img" aria-label="Modern two-storey family home at dusk with lit windows under a blue sky">
  <h1 class="abs">Selling Your Home With Us<br>Will Save You Thousands.</h1>
  <p class="abs">Don't pay 6% commission! Our MLS Flat Fee Listing Service<br>lets YOU decide how much you want to pay.</p>
  <a class="btn btn-blue b1">LEARN MORE</a>
  <a class="btn btn-red b2">LIST YOUR HOME</a>
</section>

<section class="about">
  <div class="abs ring" style="left:110px;top:806px;width:424px;height:424px"></div>
  <div class="abs photo" role="img" aria-label="Chalet-style house with warm lit windows at twilight" style="left:123px;top:819px;width:398px;height:398px;background:radial-gradient(circle at 50% 35%,#9bb8e0 0%,#3f6fb0 55%,#4b3e35 100%)"></div>
  <h2 class="abs about-title">BRIGHTKEY <span class="accent">HOME SALES</span></h2>
  <p class="abs lorem about-text">Lorem ipsum dolor sit amet, consectetur adipiscing elit, sed do eiusmod tempor incididunt ut labore et dolore magna aliquauis ipsum suspendisse ultrices gravidaus commodo viverramae cenas accumsan lacus velcilisis. Lorem ipsum dolor sit amet, consectetur adipiscing elit, sed do eiusmod tempor incididunt ut labore et dolore magna aliquauis ipsum suspendisse ultrices gravidasus commodo viverramae cenas accumsan lacus vel falisis. Lorem ipsum dolor sit amet, consectetur adipiscing elit, sed do eiusmod tempor incididun</p>
  <a class="btn btn-red" style="left:580px;top:1122px;width:170px;height:56px">READ MORE</a>
</section>

<section class="abs packages">
  <h2 class="abs section-title">OUR FLAT FEE <span class="accent">MLS LISTING</span> PACKAGES</h2>
  <div class="abs card" style="left:128px">
    <div class="abs price"><span><sup>$</sup>149*</span></div>
    <h3>GOLD</h3>
    <p>Lorem ipsum dolor<br>Sit met, consectetur<br>Qadipiscing elit, sed do<br>Dusmod tempor incididnt<br>Kabore et dolore magna<br>Ut enim ad loremsminim<br>Lstrud exercitation</p>
    <a class="btn btn-red">LIST NOW</a><a class="more">See All Features</a>
  </div>
  <div class="abs card" style="left:451px">
    <div class="abs price"><span><sup>$</sup>249*</span></div>
    <h3>PLATINUM</h3>
    <p>Lorem ipsum dolor<br>Sit met, consectetur<br>Qadipiscing elit, sed do<br>Dusmod tempor incididnt<br>Kabore et dolore magna<br>Ut enim ad loremsminim<br>Lstrud exercitation</p>
    <a class="btn btn-red">LIST NOW</a><a class="more">See All Features</a>
  </div>
  <div class="abs card" style="left:774px">
    <div class="abs price"><span><sup>$</sup>349*</span></div>
    <h3>PLATINUM+</h3>
    <p>Lorem ipsum dolor<br>Sit met, consectetur<br>Qadipiscing elit, sed do<br>Dusmod tempor incididnt<br>Kabore et dolore magna<br>Ut enim ad loremsminim<br>Lstrud exercitation</p>
    <a class="btn btn-red">LIST NOW</a><a class="more">See All Features</a>
  </div>
</section>

<section class="steps">
  <h2 class="abs section-title" style="left:0;top:2138px;width:1200px">FOUR SIMPLE STEPS<br>TO <span class="accent">SELLING YOUR</span> HOME.</h2>
  <svg class="abs" style="left:400px;top:2250px" width="400" height="390" viewBox="0 0 400 390"><path d="M10 190 A190 190 0 0 0 390 190" fill="none" stroke="#0054AA" stroke-width="5"/></svg>
  <div class="abs" role="img" aria-label="Grey two-storey house with porch" style="left:490px;top:2335px;width:225px;height:200px;background:linear-gradient(180deg,#5f6670 0%,#c9ccd1 55%,#eceff2 100%);border-radius:6px"></div>

  <div class="abs step left" style="left:110px;top:2282px;width:268px"><h4>1. Choose Your<br>Package</h4><p>Lorem ipsum dolor sit amet, cons ec tetur adipiscing elit, sed do eiusmod tempor incididunt ut</p></div>
  <div class="abs step left" style="left:90px;top:2442px;width:268px"><h4>2. Complete Online<br>Listing Forms</h4><p>Lorem ipsum dolor sit amet, cons ec tetur adipiscing elit, sed do eiusmod tempor incididunt ut</p></div>
  <div class="abs step" style="left:843px;top:2282px;width:268px"><h4>4. You Save<br>Thousands</h4><p>Lorem ipsum dolor sit amet, cons ec tetur adipiscing elit, sed do eiusmod tempor incididunt ut</p></div>
  <div class="abs step" style="left:843px;top:2442px;width:268px"><h4>3. We List You<br>On The Local MLS</h4><p>Lorem ipsum dolor sit amet, cons ec tetur adipiscing elit, sed do eiusmod tempor incididunt ut</p></div>

  <div class="abs icon" style="left:397px;top:2293px"><svg width="44" height="44" viewBox="0 0 44 44" fill="none" stroke="#fff" stroke-width="2.2"><rect x="6" y="6" width="13" height="13"/><rect x="25" y="6" width="13" height="13"/><rect x="6" y="25" width="13" height="13"/><path d="M27 31l4 4 8-9"/></svg></div>
  <div class="abs icon" style="left:380px;top:2452px"><svg width="44" height="44" viewBox="0 0 44 44" fill="none" stroke="#fff" stroke-width="2.2"><rect x="9" y="5" width="26" height="34" rx="2"/><path d="M15 14h14M15 21h14M15 28h9"/></svg></div>
  <div class="abs icon" style="left:718px;top:2293px"><svg width="44" height="44" viewBox="0 0 44 44" fill="none" stroke="#fff" stroke-width="2.2"><rect x="5" y="12" width="34" height="20" rx="2" transform="rotate(-20 22 22)"/><circle cx="22" cy="22" r="6"/></svg></div>
  <div class="abs icon" style="left:726px;top:2452px"><svg width="46" height="40" viewBox="0 0 46 40" fill="none" stroke="#fff" stroke-width="2.2"><circle cx="23" cy="12" r="7"/><path d="M10 36c0-8 6-12 13-12s13 4 13 12"/><circle cx="9" cy="15" r="5"/><circle cx="37" cy="15" r="5"/></svg></div>
</section>

<section class="abs sold">
  <h2 class="abs section-title">RECENTLY <span class="tag">SOLD</span> PROPERTIES</h2>
  <svg class="abs" style="left:70px;top:255px" width="14" height="24" viewBox="0 0 14 24"><path d="M12 2L3 12l9 10" fill="none" stroke="#555" stroke-width="2.4"/></svg>
  <svg class="abs" style="left:1107px;top:255px" width="14" height="24" viewBox="0 0 14 24"><path d="M2 2l9 10-9 10" fill="none" stroke="#555" stroke-width="2.4"/></svg>

  <div class="abs prop-img" role="img" aria-label="Dark modern three-storey townhouse" style="left:128px;background:linear-gradient(180deg,#a8c4e4 0%,#4d5560 60%,#3e4a3a 100%)"></div>
  <div class="abs prop-img" role="img" aria-label="White modern house with garage and trees" style="left:451px;background:linear-gradient(180deg,#cfe3f0 0%,#e9ebe6 55%,#6e8f58 100%)"></div>
  <div class="abs prop-img" role="img" aria-label="Brick family home lit at dusk" style="left:774px;background:linear-gradient(180deg,#3c5ea0 0%,#6a5a4c 60%,#2f3a2a 100%)"></div>

  <div class="abs prop-box" style="left:142px"><div class="val">$ 6,778</div><div class="cap">Commission Saved</div><p class="desc">Lorem ipsum dolor sit am<br>etcons ectetur adiplotis.</p><div class="rate">Sold Rate $ 3,565</div></div>
  <div class="abs prop-box" style="left:465px"><div class="val">$ 6,778</div><div class="cap">Commission Saved</div><p class="desc">Lorem ipsum dolor sit am<br>etcons ectetur adiplotis.</p><div class="rate">Sold Rate $ 3,565</div></div>
  <div class="abs prop-box" style="left:788px"><div class="val">$ 6,778</div><div class="cap">Commission Saved</div><p class="desc">Lorem ipsum dolor sit am<br>etcons ectetur adiplotis.</p><div class="rate">Sold Rate $ 3,565</div></div>
</section>

<section class="service">
  <h2 class="abs service-title">SERVICE AREAS</h2>
  <p class="abs lorem service-text">Lorem ipsum dolor sit amet, conseetur adipiscing elit, sed do eiusmod tempor incididunt ut labore et dolore magna aliquauis ipsum suspendisse ultrices gravidaus commodo viverramae cen saccumsan lacus velcilisis.</p>
  <a class="btn btn-red" style="left:131px;top:3715px;width:151px;height:48px">READ MORE</a>
  <div class="abs" role="img" aria-label="Map of the United States showing service locations" style="left:630px;top:3475px;width:540px;height:350px;background:radial-gradient(ellipse at 50% 45%,#8fb2ec 0%,#9fbdf0 60%,#ffffff 100%);border-radius:40% 45% 35% 40%"></div>
  <div class="abs loc-card"><b>Location Name</b><p>Lorem ipsum dolor sit<br>amet consectetur</p></div>
  <svg class="abs" style="left:680px;top:3590px" width="22" height="30" viewBox="0 0 22 30"><path d="M11 0C5 0 0 5 0 11c0 8 11 19 11 19s11-11 11-19C22 5 17 0 11 0z" fill="#0c3f9a"/><circle cx="11" cy="11" r="4" fill="#fff"/></svg>
</section>

<section class="abs contact">
  <div class="abs ring" style="left:165px;top:92px;width:416px;height:416px;border-color:#fff"></div>
  <div class="abs photo" role="img" aria-label="Two colleagues reviewing documents at an office desk" style="left:176px;top:103px;width:394px;height:394px;background:linear-gradient(160deg,#f2f2f2 0%,#c9c3bd 50%,#6d6a68 100%)"></div>
  <h2 class="abs">CONTACT US</h2>
  <p class="abs intro">Lorem ipsum dolor sit amet, consectetur adipiscing elit<br>sed do eiusmod tempor incididunt ut labore.</p>
</section>
<div class="field" style="left:617px;top:4125px;width:224px;height:44px">First Name:</div>
<div class="field" style="left:847px;top:4125px;width:225px;height:44px">Last Name:</div>
<div class="field" style="left:617px;top:4180px;width:224px;height:44px">Phone:</div>
<div class="field" style="left:847px;top:4180px;width:225px;height:44px">Email:</div>
<div class="field" style="left:617px;top:4235px;width:455px;height:103px">Message:</div>
<a class="btn submit" style="left:617px;top:4351px;width:116px;height:46px;background:var(--navy)">SUBMIT</a>

<footer class="footer">
  <div class="abs brand"><span class="dot"></span>Brightkey Home Sales</div>
  <div class="abs fcol" style="left:408px;top:4555px"><h4>MENU</h4><ul><li>Home</li><li>Our Services</li><li>Testimonials</li><li>Gallery</li><li>Contact</li></ul></div>
  <div class="abs fcol" style="left:585px;top:4555px"><h4>LINKS</h4><ul><li>How It Works</li><li>Pricing</li><li>Why We're Better</li><li>List your Home</li><li>Contact Us</li></ul></div>
  <div class="abs fcol" style="left:816px;top:4555px;width:260px"><h4>CONTACT</h4>
    <div class="cinfo"><span class="ci"><svg width="12" height="16" viewBox="0 0 12 16"><path d="M6 0C2.7 0 0 2.7 0 6c0 4.5 6 10 6 10s6-5.5 6-10C12 2.7 9.3 0 6 0z" fill="#fff"/><circle cx="6" cy="6" r="2" fill="#0054AA"/></svg></span><span>48 Harbor Lane, Suite 210,<br>Fairview 463.</span></div>
    <div class="cinfo"><span class="ci"><svg width="14" height="14" viewBox="0 0 14 14"><path d="M3 0l3 3-2 2c1 2 3 4 5 5l2-2 3 3-2 3C6 14 0 8 0 3z" fill="#fff"/></svg></span><span>Phone:<br>(555) 014-2290</span></div>
    <div class="cinfo"><span class="ci"><svg width="14" height="10" viewBox="0 0 14 10"><rect width="14" height="10" fill="#fff"/><path d="M0 0l7 5 7-5" fill="none" stroke="#0054AA" stroke-width="1.4"/></svg></span><span>Email:<br>hello@brightkeyhomes.com</span></div>
  </div>
  <div class="abs divider"></div>
  <div class="abs social" aria-label="Social media links"><span></span><span></span><span></span><span></span><span></span></div>
  <div class="abs copy">© 2023 Brightkey Home Sales. All rights are reserved.</div>
</footer>

</body>
</html>
```